Online radio: TunaWave homepage redesign

TunaWave is one of the world's leading brands of personalizable online radio -- similar to Melodex, but aimed at a somewhat older audience (age 35-54).

We'd like to redesign our homepage with a more contemporary look: It should emphasize our wide variety of GENRES (as the primary navigation), with the search field easy to find as a secondary navigation.

We'd like to retain our corporate color of maroon/plum. (We are not committed to the gold/yellow secondary color.)

See our current homepage at www.tunawave-example.com and our in-house attempt at an improved design at http://web4.tunawave-example.com/finder/2013ms/.

Ideally, we'd like to see designs for up to THREE different states:

(1) An initial state when users first come to the page.

(2) What the page would look like as the user is looking at channel options.

(3) What the page would look like once the media player is launched.

However, you may be able to combine (2) and (3) in a single screenshot.

Thanks!
Updates

At the request of several designers, we have decided to extend our deadline by four days. At the same time, we have increased our budget, including the addition of a 2nd place award. Thanks for your excellent work!

Thanks very much for your designs! We are very pleased with the overall quality of the work we are seeing. One reminder: As our brief says, the user interface "should emphasize our wide variety of GENRES (as the primary navigation), with the search field easy to find as a secondary navigation," and we feel that your design uses the SEARCH field as the primary navigation. Many of the designs use a large search field as the primary navigation. If yours does, you might want to tweak your design to put a greater emphasis on browsing genres as the primary navigation. Thanks and good luck!

Target Market(s)

Adults age 35-54 listening to online radio at work

Industry/Entity Type

Radio

Font styles to use
Sans Serif

Requirements
Must have
• This is a design/UI project -- we do not need code

```html
<!DOCTYPE html>
<html lang="en">
<head>
<meta charset="utf-8">
<title>TunaWave – Online Radio</title>
<link rel="stylesheet" href="https://fonts.googleapis.com/css2?family=Jost:wght@400;500;600;700&display=swap">
<style>
  :root {
    --plum: #5e1a4c;
    --plum-dark: #4a123b;
    --plum-glass: rgba(94, 26, 76, 0.82);
    --gold: #ffc515;
    --gold-deep: #f5a800;
    --white: #ffffff;
    --ink: #4a4a4a;
    --rule: #cfcfcf;
    --hero-a: #0c1a3e;
    --hero-b: #26336e;
    --hero-c: #4a2a55;
  }
  * { box-sizing: border-box; margin: 0; padding: 0; }
  html, body { width: 1200px; height: 906px; overflow: hidden; }
  body { font-family: "Jost", "Futura", sans-serif; color: var(--white); position: relative; background: var(--hero-a); }

  .site-header { position: absolute; left: 0; top: 0; width: 1200px; height: 66px; background: var(--plum); border-bottom: 1px solid #7a3a68; z-index: 2; }
  .brand { position: absolute; left: 100px; top: 9px; display: flex; align-items: center; gap: 6px; }
  .brand-dot { width: 44px; height: 44px; border-radius: 50%; background: var(--gold); }
  .brand-name { font-size: 34px; font-weight: 500; color: var(--white); letter-spacing: -0.5px; }
  .header-nav { position: absolute; right: 99px; top: 18px; display: flex; align-items: center; height: 28px; font-size: 15px; font-weight: 600; }
  .header-nav .sep { width: 1px; height: 16px; background: rgba(255,255,255,.5); margin: 0 13px; }
  .header-nav svg { display: block; }

  .hero { position: absolute; left: 0; top: 66px; width: 1200px; height: 790px;
    background: radial-gradient(ellipse at 25% 30%, var(--hero-b) 0%, transparent 55%),
                radial-gradient(ellipse at 80% 85%, #6a6c82 0%, transparent 40%),
                linear-gradient(135deg, var(--hero-c) 0%, var(--hero-a) 55%, #0a0f24 100%); }

  .headline { position: absolute; left: 0; top: 128px; width: 1200px; text-align: center; font-size: 31px; font-weight: 500; line-height: 38px; letter-spacing: 0.2px; }
  .headline em { font-style: normal; color: var(--gold); font-weight: 600; }

  /* Search is secondary: compact and quieter than the genre bar */
  .search { position: absolute; left: 340px; top: 236px; width: 520px; height: 46px; display: flex; }
  .search-field { flex: 1; background: var(--white); border-radius: 3px 0 0 3px; color: #666; font-size: 17px; padding: 12px 12px; }
  .search-button { width: 58px; background: var(--plum); border-radius: 0 3px 3px 0; display: flex; align-items: center; justify-content: center; }
  .search-hint { position: absolute; left: 0; top: 298px; width: 1200px; text-align: center; font-size: 14px; opacity: .9; }

  .tabs { position: absolute; top: 389px; left: 118px; display: flex; gap: 13px; }
  .tab { width: 182px; height: 44px; border-radius: 6px 6px 0 0; background: linear-gradient(var(--gold), var(--gold-deep)); color: var(--plum); font-size: 16px; font-weight: 600; text-align: center; line-height: 44px; }
  .tab.is-active { background: var(--plum); color: var(--white); }

  .channel-panel { position: absolute; left: 100px; top: 433px; width: 1000px; height: 329px; background: var(--white); border: 1px solid #bbb; }
  .panel-title { position: absolute; top: 22px; left: 104px; width: 762px; display: flex; align-items: center; gap: 12px; color: var(--plum); font-size: 17px; font-weight: 600; }
  .panel-title::before, .panel-title::after { content: ""; flex: 1; height: 1px; background: var(--rule); }
  .channel { position: absolute; top: 66px; width: 176px; text-align: center; }
  .channel-art { width: 168px; height: 108px; margin: 0 auto; border: 2px solid #444; }
  .channel-name { margin-top: 10px; color: var(--plum); font-size: 15px; font-weight: 700; line-height: 18px; }
  .channel-desc { color: var(--ink); font-size: 14px; line-height: 18px; }
  .play { display: inline-flex; align-items: center; gap: 5px; margin-top: 7px; height: 25px; padding: 0 8px 0 5px; border-radius: 13px; background: var(--plum); color: var(--gold); font-size: 14px; font-weight: 700; }
  .play-icon { width: 16px; height: 16px; border-radius: 50%; background: var(--white); display: flex; align-items: center; justify-content: center; }
  .scroll-track { position: absolute; left: 10px; top: 305px; width: 982px; height: 1px; background: #999; }
  .scroll-thumb { position: absolute; left: 25px; top: 299px; width: 67px; height: 12px; background: var(--gold); }

  /* Genres are the primary navigation: full-width band, larger type */
  .genre-bar { position: absolute; top: 778px; left: 0; width: 1200px; height: 78px; background: var(--plum-glass); border-top: 3px solid var(--gold); font-size: 18px; font-weight: 700; letter-spacing: 0.3px; }
  .genre-bar span { position: absolute; top: 24px; transform: translateX(-50%); white-space: nowrap; }
  .genre-bar span::after { content: ""; position: absolute; left: 50%; bottom: -6px; width: 24px; height: 2px; margin-left: -12px; background: var(--gold); }

  .site-footer { position: absolute; left: 0; top: 856px; width: 1200px; height: 50px; background: var(--plum-dark); }
  .footer-links { position: absolute; left: 100px; top: 19px; display: flex; gap: 21px; font-size: 12px; font-weight: 500; letter-spacing: -0.2px; }
  .social { position: absolute; right: 121px; top: 14px; display: flex; gap: 9px; }
  .social span { width: 26px; height: 26px; border-radius: 50%; background: var(--white); }
</style>
</head>
<body>
  <header class="site-header">
    <div class="brand"><span class="brand-dot"></span><span class="brand-name">TunaWave</span></div>
    <nav class="header-nav">
      <svg width="22" height="22" viewBox="0 0 22 22" aria-label="Random station"><rect x="2" y="2" width="18" height="18" rx="4" fill="#e8e0e6"/><circle cx="7" cy="7" r="1.6" fill="#5e1a4c"/><circle cx="15" cy="7" r="1.6" fill="#5e1a4c"/><circle cx="11" cy="11" r="1.6" fill="#5e1a4c"/><circle cx="7" cy="15" r="1.6" fill="#5e1a4c"/><circle cx="15" cy="15" r="1.6" fill="#5e1a4c"/></svg>
      <span class="sep"></span>
      <svg width="24" height="24" viewBox="0 0 24 24" aria-label="Help"><circle cx="12" cy="12" r="11" fill="#fff"/><text x="12" y="17" text-anchor="middle" font-family="Jost, sans-serif" font-weight="700" font-size="15" fill="#5e1a4c">?</text></svg>
      <span class="sep"></span>
      <span>LOG IN</span>
      <span class="sep"></span>
      <span>JOIN FOR FREE</span>
    </nav>
  </header>

  <main class="hero" role="img" aria-label="Concert photo of a singer playing a keytar under blue stage lights"></main>

  <h1 class="headline">THOUSANDS OF<br><em>RADIO STATIONS</em> WITH ENDLESS MUSIC</h1>

  <form class="search">
    <div class="search-field">Find the radio that plays your favorite music</div>
    <div class="search-button">
      <svg width="22" height="22" viewBox="0 0 26 26"><circle cx="11" cy="11" r="7.5" fill="none" stroke="#fff" stroke-width="4"/><line x1="16.5" y1="16.5" x2="22" y2="22" stroke="#fff" stroke-width="5" stroke-linecap="round"/></svg>
    </div>
  </form>
  <p class="search-hint">For Example : Search by Artist or Keyword etc</p>

  <nav class="tabs">
    <div class="tab">MY HISTORY</div>
    <div class="tab">MY FAVORITE</div>
    <div class="tab is-active">MOST POPULAR</div>
    <div class="tab">WORKDAY MOODS</div>
    <div class="tab">GENRES</div>
  </nav>

  <section class="channel-panel">
    <h2 class="panel-title">MOST POPULAR CHANNELS</h2>

    <article class="channel" style="left:5px">
      <div class="channel-art" role="img" aria-label="Artist photo: pop singer in a jewelled headband" style="background:linear-gradient(135deg,#d9c7a8,#7a5a3c)"></div>
      <h3 class="channel-name">Magic Sunny Lite Mix</h3>
      <p class="channel-desc">Today's best adult hit music,<br>some softer...</p>
      <span class="play"><span class="play-icon"><svg width="8" height="8" viewBox="0 0 8 8"><path d="M1 0L8 4L1 8Z" fill="#5e1a4c"/></svg></span>PLAY</span>
    </article>
    <article class="channel" style="left:210px">
      <div class="channel-art" role="img" aria-label="Artist photo: singer performing at a microphone" style="background:linear-gradient(135deg,#2a3f8a,#0e1430)"></div>
      <h3 class="channel-name">Magic Sunny Lite Mix</h3>
      <p class="channel-desc">Today's best adult hit music,<br>some softer...</p>
      <span class="play"><span class="play-icon"><svg width="8" height="8" viewBox="0 0 8 8"><path d="M1 0L8 4L1 8Z" fill="#5e1a4c"/></svg></span>PLAY</span>
    </article>
    <article class="channel" style="left:412px">
      <div class="channel-art" role="img" aria-label="Artist photo: singer seated by a window" style="background:linear-gradient(135deg,#9aa07a,#3a3a30)"></div>
      <h3 class="channel-name">Magic Sunny Lite Mix</h3>
      <p class="channel-desc">Today's best adult hit music,<br>some softer...</p>
      <span class="play"><span class="play-icon"><svg width="8" height="8" viewBox="0 0 8 8"><path d="M1 0L8 4L1 8Z" fill="#5e1a4c"/></svg></span>PLAY</span>
    </article>
    <article class="channel" style="left:615px">
      <div class="channel-art" role="img" aria-label="Artist photo: singer in a grey hoodie" style="background:linear-gradient(135deg,#e8eef4,#8a96a6)"></div>
      <h3 class="channel-name">Magic Sunny Lite Mix</h3>
      <p class="channel-desc">Today's best adult hit music,<br>some softer...</p>
      <span class="play"><span class="play-icon"><svg width="8" height="8" viewBox="0 0 8 8"><path d="M1 0L8 4L1 8Z" fill="#5e1a4c"/></svg></span>PLAY</span>
    </article>
    <article class="channel" style="left:816px">
      <div class="channel-art" role="img" aria-label="Artist photo: rock singer on stage at a microphone" style="background:linear-gradient(135deg,#6a1a1a,#1a1010)"></div>
      <h3 class="channel-name">Magic Sunny Lite Mix</h3>
      <p class="channel-desc">Today's best adult hit music,<br>some softer...</p>
      <span class="play"><span class="play-icon"><svg width="8" height="8" viewBox="0 0 8 8"><path d="M1 0L8 4L1 8Z" fill="#5e1a4c"/></svg></span>PLAY</span>
    </article>

    <div class="scroll-track"></div>
    <div class="scroll-thumb"></div>
  </section>

  <nav class="genre-bar" aria-label="Genres">
    <span style="left:205px">TOP 40 / POP HITS</span>
    <span style="left:375px">LITE HITS</span>
    <span style="left:516px">COUNTRY</span>
    <span style="left:649px">CLASSICAL</span>
    <span style="left:812px">CLASSIC ROCK</span>
    <span style="left:991px">SMOOTH JAZZ</span>
  </nav>

  <footer class="site-footer">
    <nav class="footer-links"><span>HELP</span><span>ABOUT &amp; CONTACT</span><span>MOBILE</span></nav>
    <div class="social">
      <span aria-label="Social link"></span>
      <span aria-label="Social link"></span>
      <span aria-label="Social link"></span>
      <span aria-label="Social link"></span>
    </div>
  </footer>
</body>
</html>
```